Sprinkles & Tails 2nd Annual Fundraiser

I am a Realtor sponsoring the 2nd annual fundraiser on behalf of Allies of Harlow Vale Animal Haven. Like the flyer to be professional yet fun and inviting. Please see the attached file below. The 1st annual flyer was fun but not as professional, modern or inviting as I would have liked it to be.
Target Market(s)
Dog lovers in Ponte Vedra, Ponte Vedra Beach and Nocatee Florida
Logo Text
Needed
Font styles to use
Other font styles liked:
- Font that fits the style of the fundraiser
Colors
886aae
abd036
Requirements
Must have
- Please see the attached flyer and photos.
- This will be the 2nd Annual on Saturday, April 27, 2019 from 10AM - 1PM. Same location: Kendrick Realty, 418 Tillbrook Ave. Ponte Vedra FL 32075

```html
<!DOCTYPE html>
<html lang="en">
<head>
<meta charset="utf-8">
<title>Sprinkles &amp; Tails Doggie Wash Extravaganza</title>
<link rel="stylesheet" href="https://fonts.googleapis.com/css2?family=Bowlby+One&family=Arimo:ital,wght@0,400;0,700;1,700&family=Roboto+Condensed:wght@700&display=swap">
<style>
  :root {
    --purple: #7f6bb3;
    --purple-deep: #6d5aa3;
    --green: #abd036;
    --white: #ffffff;
    --ink: #1e1e1e;
    --accent: #e88a1a;
  }
  html, body { margin: 0; padding: 0; overflow: hidden; }
  body { width: 927px; height: 1200px; background: var(--white); }
  .flyer { position: relative; width: 927px; height: 1200px; overflow: hidden; background: var(--white); font-family: "Arimo", Arial, sans-serif; }
  .abs { position: absolute; }

  .photo { position: absolute; }
  .photo-mascot { left: 520px; top: 96px; width: 407px; height: 520px;
    background: radial-gradient(ellipse 60% 62% at 62% 50%, rgba(172,96,58,0.38) 0%, rgba(196,130,96,0.22) 55%, rgba(255,255,255,0) 100%); }
  .photo-dog { left: 26px; top: 128px; width: 154px; height: 204px; background: linear-gradient(165deg, #e4e1df 0%, #b3aca6 55%, #d9a3bf 100%); }
  .photo-crowd { left: 536px; top: 564px; width: 391px; height: 292px; background: linear-gradient(180deg, #cfe0ea 0%, #b7c7b3 30%, #c4bfb6 62%, #e0dcd4 100%); }
  .photo-owner { left: 656px; top: 862px; width: 271px; height: 338px; background: linear-gradient(180deg, #eef0f4 0%, #dcdfe5 48%, #d2b08e 80%, #e0c6a8 100%); }

  .headline { font-family: "Bowlby One", "Arial Black", sans-serif; font-style: italic; line-height: 1; margin: 0; white-space: nowrap; transform: skewX(-8deg); transform-origin: left bottom; }
  .title-annual { left: 30px; top: -6px; font-size: 120px; color: var(--green); }
  .title-name-1 { left: 196px; top: 140px; font-size: 72px; color: var(--purple); }
  .title-name-2 { left: 196px; top: 222px; font-size: 72px; color: var(--purple); }
  .title-name-2 .amp { color: var(--green); }
  .title-wash { left: 12px; top: 306px; font-size: 84px; color: var(--purple); }
  .title-extra { left: 12px; top: 400px; font-size: 78px; color: var(--purple); }

  .tagline { left: 14px; top: 486px; width: 672px; height: 62px; }

  .donate { left: 700px; top: 466px; width: 226px; height: 152px; }
  .date-cloud { left: 14px; top: 556px; width: 280px; height: 214px; }
  .address-cloud { left: 336px; top: 560px; width: 316px; height: 220px; }
  .hours { left: 10px; top: 680px; width: 340px; height: 160px; }
  .notice { left: 306px; top: 800px; width: 340px; height: 320px; }

  .features { left: 12px; top: 874px; margin: 0; padding: 0; list-style: none; }
  .features li { display: flex; align-items: center; height: 35.4px; font-weight: 700; font-style: italic; font-size: 22px; color: var(--purple); }
  .features .dot { width: 14px; height: 14px; border-radius: 50%; background: var(--accent); margin: 0 22px 0 4px; flex: none; }

  .footer { left: 0; top: 1116px; width: 927px; height: 84px; background: var(--purple); }
  .brand-box { position: absolute; top: 1127px; height: 64px; background: var(--white); display: flex; align-items: center; justify-content: center; gap: 5px; text-align: center; font-weight: 700; color: var(--purple-deep); line-height: 1.1; }
  .brand-realtor { left: 10px; width: 128px; font-size: 13px; }
  .brand-haven { left: 364px; width: 78px; font-size: 10px; }
  .brand-mark { width: 9px; height: 9px; border-radius: 50%; background: var(--purple-deep); flex: none; }
  .contact { position: absolute; top: 1126px; color: var(--white); font-size: 12.4px; line-height: 1.28; }
  .contact .name { font-size: 17px; font-weight: 700; font-style: italic; line-height: 1.15; }
  .contact-realtor { left: 146px; }
  .contact-haven { left: 448px; }
</style>
</head>
<body>
<main class="flyer">
  <div class="photo photo-mascot" role="img" aria-label="Photo of a person in a brown and white dog mascot costume waving"></div>
  <div class="photo photo-dog" role="img" aria-label="Photo of a shaggy grey dog in a pink bandana beside the event sign"></div>
  <div class="photo photo-crowd" role="img" aria-label="Photo of volunteers washing dogs outdoors at last year's event"></div>
  <div class="photo photo-owner" role="img" aria-label="Photo of a smiling woman hugging a tan dog next to the event sign"></div>

  <h1 class="abs headline title-annual">2nd Annual</h1>
  <p class="abs headline title-name-1">Sprinkles</p>
  <p class="abs headline title-name-2"><span class="amp">&amp;</span> Tails</p>
  <p class="abs headline title-wash">Doggie Wash</p>
  <p class="abs headline title-extra">Extravaganza</p>

  <svg class="abs tagline" viewBox="0 0 672 62" aria-label="A Family Fun Event for All Ages">
    <polygon points="2,4 672,22 668,62 6,40" fill="var(--green)"/>
    <text x="336" y="40" text-anchor="middle" transform="rotate(1.6 336 32)" font-family="Arimo, Arial, sans-serif" font-weight="700" font-style="italic" font-size="31" fill="var(--white)">A Family Fun Event for All Ages</text>
  </svg>

  <svg class="abs donate" viewBox="0 0 226 152">
    <g transform="rotate(-12 113 76)">
      <ellipse cx="113" cy="76" rx="106" ry="58" fill="var(--white)" stroke="var(--purple)" stroke-width="5"/>
      <g font-family="Roboto Condensed, Arial Narrow, sans-serif" font-weight="700" fill="var(--purple-deep)" text-anchor="middle">
        <text x="113" y="62" font-size="15">To make a donation:</text>
        <text x="113" y="82" font-size="14">https://www.allieshv.org/give</text>
        <circle cx="86" cy="98" r="6" fill="var(--green)"/>
        <text x="122" y="104" font-size="15">Donate</text>
      </g>
    </g>
  </svg>

  <svg class="abs date-cloud" viewBox="0 0 280 214">
    <g fill="var(--green)">
      <ellipse cx="140" cy="108" rx="118" ry="82"/>
      <circle cx="70" cy="70" r="58"/><circle cx="150" cy="58" r="56"/><circle cx="214" cy="84" r="56"/>
      <circle cx="58" cy="140" r="56"/><circle cx="140" cy="150" r="60"/><circle cx="220" cy="146" r="52"/>
    </g>
    <g transform="rotate(-9 140 107)" font-family="Arimo, Arial, sans-serif" font-weight="700" fill="var(--purple)" text-anchor="middle" font-size="34">
      <text x="146" y="80">Saturday,</text>
      <text x="146" y="122">April 27,</text>
      <text x="146" y="164">2019</text>
    </g>
  </svg>

  <svg class="abs hours" viewBox="0 0 340 160" aria-label="from 10AM - 1PM">
    <defs><path id="hoursArc" d="M 16 108 Q 170 150 330 20"/></defs>
    <text font-family="Roboto Condensed, Arial Narrow, sans-serif" font-weight="700" font-size="42" fill="var(--purple)"><textPath href="#hoursArc">from 10AM - 1PM</textPath></text>
  </svg>

  <svg class="abs address-cloud" viewBox="0 0 316 220">
    <g fill="var(--purple)">
      <ellipse cx="158" cy="110" rx="132" ry="86"/>
      <circle cx="66" cy="64" r="56"/><circle cx="150" cy="54" r="54"/><circle cx="240" cy="80" r="60"/>
      <circle cx="70" cy="150" r="56"/><circle cx="168" cy="160" r="58"/><circle cx="256" cy="156" r="54"/>
    </g>
    <g transform="rotate(12 158 110)" font-family="Roboto Condensed, Arial Narrow, sans-serif" font-weight="700" fill="var(--white)" text-anchor="middle" font-size="31">
      <text x="156" y="56">Kendrick Realty,</text>
      <text x="156" y="92">418 Tillbrook Ave.</text>
      <text x="156" y="128">Ponte Vedra</text>
      <text x="156" y="164">FL 32075</text>
    </g>
  </svg>

  <svg class="abs notice" viewBox="0 0 340 320">
    <polygon points="8,6 150,62 334,48 270,150 300,312 190,238 90,250 120,150" fill="var(--green)"/>
    <g transform="rotate(10 180 150)" font-family="Arimo, Arial, sans-serif" font-size="17" fill="var(--ink)" text-anchor="middle">
      <text x="180" y="108">All domestic breeds</text>
      <text x="180" y="128">from puppies to</text>
      <text x="180" y="148">seniors invited.</text>
      <text x="180" y="168">Please be sure <tspan fill="var(--white)" font-weight="700">Furry</tspan></text>
      <text x="180" y="188"><tspan fill="var(--white)" font-weight="700">Fido</tspan> is tolerant of</text>
      <text x="180" y="208">other dogs, crowds</text>
      <text x="180" y="228">and bathing.</text>
    </g>
  </svg>

  <ul class="abs features">
    <li><span class="dot"></span>FREE Doggie Wash</li>
    <li><span class="dot"></span>Food &amp; Beverages</li>
    <li><span class="dot"></span>Vendors (FREE give-a-ways)</li>
    <li><span class="dot"></span>Raffle Drawings</li>
    <li><span class="dot"></span>Grand Prize</li>
    <li><span class="dot"></span>Donations Welcome</li>
  </ul>

  <footer>
    <div class="abs footer"></div>
    <div class="brand-box brand-realtor"><span class="brand-mark"></span>Marianne Keller</div>
    <div class="contact contact-realtor">
      <div class="name">Marianne Keller</div>
      <div>Kendrick Realty Corp.</div>
      <div>770.555.0148</div>
      <div>mkeller@kendrickrealtycorp.com</div>
    </div>
    <div class="brand-box brand-haven">Allies of Harlow Vale Animal Haven</div>
    <div class="contact contact-haven">
      <div class="name">Denise Corwin</div>
      <div>AHVAH</div>
      <div>904.555.0192</div>
      <div>denise.corwin@mailbay.net</div>
    </div>
  </footer>
</main>
</body>
</html>
```